Total Health and Wellness Infographic

Hello,
We need an infographic of the 16 factors for total health and wellness.  We are imagining a circle pie chart with all 16 categories, with each pie having a corresponding graphic in it.
We want it to be modern, beautiful, easy to understand (we welcome cartoon graphics)
The 16 points are:
a. Sleep
b. Exercise/Movement
c. Macronutrient Diet
d. Micronutrients
e. Health Habits (Tracking, Morning Routines, Mindfulness/Meditation)
f. CV Health
g. GI Health
h. Brain Health
i. Inflammation (Food allergies, etc)
j. Hormone Health
k. Stress
l. Immunity and Cancer Detection/ Prevention
m. Detoxification – heavy metals, pesticides, your environment
n. Longevity
o. Sexual Health
p. Aesthetics – Facial, Hair, Body
Attached are our brand standards for reference.
Let us know if you have any questions.
Thank you!

```html
<!DOCTYPE html>
<html lang="en">
<head>
<meta charset="utf-8">
<title>The 16 Factors for Total Health and Wellness</title>
<link href="https://fonts.googleapis.com/css2?family=Antonio:wght@200;300&family=Share+Tech+Mono&display=swap" rel="stylesheet">
<style>
  :root {
    --bg-deep: #07405a;
    --bg-mid: #1683a6;
    --bg-glow: #5fd0ea;
    --bubble: #63c8e2;
    --bubble-edge: #8fdcef;
    --disc-inner: #3d86a6;
    --disc-outer: #0e3350;
    --spoke: #1b2429;
    --knob: #2c363c;
    --hub-light: #6fcbe3;
    --hub-dark: #1b6888;
    --ink: #ffffff;
  }
  html, body {
    margin: 0;
    padding: 0;
    width: 800px;
    height: 1200px;
    overflow: hidden;
  }
  body {
    background: radial-gradient(ellipse 520px 560px at 400px 740px, var(--bg-glow) 0%, var(--bg-mid) 55%, var(--bg-deep) 100%);
    font-family: "Share Tech Mono", monospace;
    color: var(--ink);
  }
  .poster {
    position: relative;
    width: 800px;
    height: 1200px;
  }
  .poster-title {
    position: absolute;
    top: 132px;
    left: 0;
    width: 800px;
    margin: 0;
    text-align: center;
    font-family: "Antonio", sans-serif;
    font-weight: 200;
    font-size: 60px;
    line-height: 57px;
    letter-spacing: 0.5px;
    text-transform: uppercase;
    color: var(--ink);
  }
  .wheel {
    position: absolute;
    top: 0;
    left: 0;
  }
  .factor-label {
    font-family: "Share Tech Mono", monospace;
    font-size: 10.5px;
    letter-spacing: 2.2px;
    fill: var(--ink);
    text-transform: uppercase;
  }
  .hub-label {
    font-family: "Antonio", sans-serif;
    font-weight: 300;
    font-size: 36px;
    fill: var(--ink);
  }
  .factor-dot { fill: var(--ink); }
  .bubble { fill: var(--bubble); }
  .icon-slot { fill: var(--ink); opacity: 0.88; }
  .spoke { stroke: var(--spoke); stroke-width: 3; }
  .knob { fill: url(#knobShade); }
</style>
</head>
<body>
<main class="poster">
  <h1 class="poster-title">The 16 Factors for<br>Total Health and Wellness</h1>

  <svg class="wheel" width="800" height="1200" viewBox="0 0 800 1200" aria-label="Wheel of the 16 health and wellness factors">
    <defs>
      <radialGradient id="discShade" cx="50%" cy="50%" r="50%">
        <stop offset="0%" stop-color="var(--disc-inner)"/>
        <stop offset="70%" stop-color="#1c5274"/>
        <stop offset="100%" stop-color="var(--disc-outer)"/>
      </radialGradient>
      <radialGradient id="hubShade" cx="50%" cy="45%" r="55%">
        <stop offset="0%" stop-color="var(--hub-light)"/>
        <stop offset="100%" stop-color="var(--hub-dark)"/>
      </radialGradient>
      <radialGradient id="bubbleShade" cx="50%" cy="50%" r="50%">
        <stop offset="60%" stop-color="var(--bubble)"/>
        <stop offset="100%" stop-color="var(--bubble-edge)"/>
      </radialGradient>
      <radialGradient id="knobShade" cx="40%" cy="35%" r="60%">
        <stop offset="0%" stop-color="#4a565c"/>
        <stop offset="100%" stop-color="var(--knob)"/>
      </radialGradient>
    </defs>

    <g class="wheel-body" transform="translate(400 732)">
      <!-- icon bubbles -->
      <g class="bubbles">
        <circle class="bubble" fill="url(#bubbleShade)" transform="rotate(11.25)" cx="0" cy="-300" r="62"/>
        <circle class="bubble" fill="url(#bubbleShade)" transform="rotate(33.75)" cx="0" cy="-300" r="62"/>
        <circle class="bubble" fill="url(#bubbleShade)" transform="rotate(56.25)" cx="0" cy="-300" r="62"/>
        <circle class="bubble" fill="url(#bubbleShade)" transform="rotate(78.75)" cx="0" cy="-300" r="62"/>
        <circle class="bubble" fill="url(#bubbleShade)" transform="rotate(101.25)" cx="0" cy="-300" r="62"/>
        <circle class="bubble" fill="url(#bubbleShade)" transform="rotate(123.75)" cx="0" cy="-300" r="62"/>
        <circle class="bubble" fill="url(#bubbleShade)" transform="rotate(146.25)" cx="0" cy="-300" r="62"/>
        <circle class="bubble" fill="url(#bubbleShade)" transform="rotate(168.75)" cx="0" cy="-300" r="62"/>
        <circle class="bubble" fill="url(#bubbleShade)" transform="rotate(191.25)" cx="0" cy="-300" r="62"/>
        <circle class="bubble" fill="url(#bubbleShade)" transform="rotate(213.75)" cx="0" cy="-300" r="62"/>
        <circle class="bubble" fill="url(#bubbleShade)" transform="rotate(236.25)" cx="0" cy="-300" r="62"/>
        <circle class="bubble" fill="url(#bubbleShade)" transform="rotate(258.75)" cx="0" cy="-300" r="62"/>
        <circle class="bubble" fill="url(#bubbleShade)" transform="rotate(281.25)" cx="0" cy="-300" r="62"/>
        <circle class="bubble" fill="url(#bubbleShade)" transform="rotate(303.75)" cx="0" cy="-300" r="62"/>
        <circle class="bubble" fill="url(#bubbleShade)" transform="rotate(326.25)" cx="0" cy="-300" r="62"/>
        <circle class="bubble" fill="url(#bubbleShade)" transform="rotate(348.75)" cx="0" cy="-300" r="62"/>
      </g>

      <!-- main disc -->
      <circle class="disc" cx="0" cy="0" r="276" fill="url(#discShade)"/>

      <!-- spokes -->
      <g class="spokes">
        <line class="spoke" transform="rotate(0)" x1="0" y1="0" x2="0" y2="-330"/>
        <line class="spoke" transform="rotate(22.5)" x1="0" y1="0" x2="0" y2="-330"/>
        <line class="spoke" transform="rotate(45)" x1="0" y1="0" x2="0" y2="-330"/>
        <line class="spoke" transform="rotate(67.5)" x1="0" y1="0" x2="0" y2="-330"/>
        <line class="spoke" transform="rotate(90)" x1="0" y1="0" x2="0" y2="-330"/>
        <line class="spoke" transform="rotate(112.5)" x1="0" y1="0" x2="0" y2="-330"/>
        <line class="spoke" transform="rotate(135)" x1="0" y1="0" x2="0" y2="-330"/>
        <line class="spoke" transform="rotate(157.5)" x1="0" y1="0" x2="0" y2="-330"/>
        <line class="spoke" transform="rotate(180)" x1="0" y1="0" x2="0" y2="-330"/>
        <line class="spoke" transform="rotate(202.5)" x1="0" y1="0" x2="0" y2="-330"/>
        <line class="spoke" transform="rotate(225)" x1="0" y1="0" x2="0" y2="-330"/>
        <line class="spoke" transform="rotate(247.5)" x1="0" y1="0" x2="0" y2="-330"/>
        <line class="spoke" transform="rotate(270)" x1="0" y1="0" x2="0" y2="-330"/>
        <line class="spoke" transform="rotate(292.5)" x1="0" y1="0" x2="0" y2="-330"/>
        <line class="spoke" transform="rotate(315)" x1="0" y1="0" x2="0" y2="-330"/>
        <line class="spoke" transform="rotate(337.5)" x1="0" y1="0" x2="0" y2="-330"/>
      </g>

      <!-- spoke knobs -->
      <g class="knobs">
        <circle class="knob" transform="rotate(0)" cx="0" cy="-330" r="11"/>
        <circle class="knob" transform="rotate(22.5)" cx="0" cy="-330" r="11"/>
        <circle class="knob" transform="rotate(45)" cx="0" cy="-330" r="11"/>
        <circle class="knob" transform="rotate(67.5)" cx="0" cy="-330" r="11"/>
        <circle class="knob" transform="rotate(90)" cx="0" cy="-330" r="11"/>
        <circle class="knob" transform="rotate(112.5)" cx="0" cy="-330" r="11"/>
        <circle class="knob" transform="rotate(135)" cx="0" cy="-330" r="11"/>
        <circle class="knob" transform="rotate(157.5)" cx="0" cy="-330" r="11"/>
        <circle class="knob" transform="rotate(180)" cx="0" cy="-330" r="11"/>
        <circle class="knob" transform="rotate(202.5)" cx="0" cy="-330" r="11"/>
        <circle class="knob" transform="rotate(225)" cx="0" cy="-330" r="11"/>
        <circle class="knob" transform="rotate(247.5)" cx="0" cy="-330" r="11"/>
        <circle class="knob" transform="rotate(270)" cx="0" cy="-330" r="11"/>
        <circle class="knob" transform="rotate(292.5)" cx="0" cy="-330" r="11"/>
        <circle class="knob" transform="rotate(315)" cx="0" cy="-330" r="11"/>
        <circle class="knob" transform="rotate(337.5)" cx="0" cy="-330" r="11"/>
      </g>

      <!-- icon slots -->
      <g class="icon-slots">
        <circle class="icon-slot" role="img" aria-label="Exercise icon: figure in motion" transform="rotate(11.25)" cx="0" cy="-316" r="20"/>
        <circle class="icon-slot" role="img" aria-label="Macronutrient diet icon: carrot on a fork" transform="rotate(33.75)" cx="0" cy="-316" r="20"/>
        <circle class="icon-slot" role="img" aria-label="Micronutrients icon: molecule structure" transform="rotate(56.25)" cx="0" cy="-316" r="20"/>
        <circle class="icon-slot" role="img" aria-label="Health habits icon: meditating figure" transform="rotate(78.75)" cx="0" cy="-316" r="20"/>
        <circle class="icon-slot" role="img" aria-label="Cardiovascular health icon: medical caduceus" transform="rotate(101.25)" cx="0" cy="-316" r="20"/>
        <circle class="icon-slot" role="img" aria-label="GI health icon: digestive tract" transform="rotate(123.75)" cx="0" cy="-316" r="20"/>
        <circle class="icon-slot" role="img" aria-label="Brain health icon: brain" transform="rotate(146.25)" cx="0" cy="-316" r="20"/>
        <circle class="icon-slot" role="img" aria-label="Inflammation icon: wheat and nuts" transform="rotate(168.75)" cx="0" cy="-316" r="20"/>
        <circle class="icon-slot" role="img" aria-label="Stress icon: burst shape" transform="rotate(191.25)" cx="0" cy="-316" r="20"/>
        <circle class="icon-slot" role="img" aria-label="Hormone health icon: linked molecule" transform="rotate(213.75)" cx="0" cy="-316" r="20"/>
        <circle class="icon-slot" role="img" aria-label="Immunity icon: shield" transform="rotate(236.25)" cx="0" cy="-316" r="20"/>
        <circle class="icon-slot" role="img" aria-label="Detoxification icon: hazard symbol" transform="rotate(258.75)" cx="0" cy="-316" r="20"/>
        <circle class="icon-slot" role="img" aria-label="Longevity icon: leaf" transform="rotate(281.25)" cx="0" cy="-316" r="20"/>
        <circle class="icon-slot" role="img" aria-label="Sexual health icon: heart" transform="rotate(303.75)" cx="0" cy="-316" r="20"/>
        <circle class="icon-slot" role="img" aria-label="Aesthetics icon: standing figure" transform="rotate(326.25)" cx="0" cy="-316" r="20"/>
        <circle class="icon-slot" role="img" aria-label="Sleep icon: figure resting in bed" transform="rotate(348.75)" cx="0" cy="-316" r="20"/>
      </g>

      <!-- hub -->
      <circle class="hub" cx="0" cy="0" r="80" fill="url(#hubShade)"/>
      <text class="hub-label" x="0" y="13" text-anchor="middle">THE 16 POINTS</text>
    </g>

    <!-- factor labels -->
    <g class="factor-labels">
      <circle class="factor-dot" cx="321" cy="514" r="3"/>
      <text class="factor-label" x="328" y="518">Sleep</text>

      <circle class="factor-dot" cx="412" cy="501" r="3"/>
      <text class="factor-label" x="419" y="505">Exercise<tspan x="419" dy="13">Movement</tspan></text>

      <circle class="factor-dot" cx="499" cy="522" r="3"/>
      <text class="factor-label" x="506" y="526">Macronutrient<tspan x="506" dy="13">Diet</tspan></text>

      <circle class="factor-dot" cx="570" cy="574" r="3"/>
      <text class="factor-label" x="563" y="578" text-anchor="end">Micronutrients</text>

      <circle class="factor-dot" cx="618" cy="652" r="3"/>
      <text class="factor-label" x="611" y="658" text-anchor="end">Health Habits<tspan x="611" dy="13">(Tracking, Morning</tspan><tspan x="611" dy="13">Routines</tspan><tspan x="611" dy="13">Mindfulness</tspan><tspan x="611" dy="13">Meditation)</tspan></text>

      <circle class="factor-dot" cx="632" cy="742" r="3"/>
      <text class="factor-label" x="625" y="746" text-anchor="end">CV Health</text>

      <circle class="factor-dot" cx="610" cy="830" r="3"/>
      <text class="factor-label" x="603" y="835" text-anchor="end">GI Health</text>

      <circle class="factor-dot" cx="555" cy="903" r="3"/>
      <text class="factor-label" x="548" y="907" text-anchor="end">Brain Health</text>

      <circle class="factor-dot" cx="478" cy="950" r="3"/>
      <text class="factor-label" x="485" y="954">Inflammation<tspan x="485" dy="13">(Food Allergies, Etc)</tspan></text>

      <circle class="factor-dot" cx="389" cy="963" r="3"/>
      <text class="factor-label" x="397" y="967">Stress</text>

      <circle class="factor-dot" cx="301" cy="941" r="3"/>
      <text class="factor-label" x="308" y="945">Hormone Health</text>

      <circle class="factor-dot" cx="228" cy="887" r="3"/>
      <text class="factor-label" x="236" y="891">Immunity and Cancer<tspan x="236" dy="13">Detection/Prevention</tspan></text>

      <circle class="factor-dot" cx="181" cy="810" r="3"/>
      <text class="factor-label" x="188" y="814">Detoxification –<tspan x="188" dy="13">Heavy Metals,</tspan><tspan x="188" dy="13">Pesticides,</tspan><tspan x="188" dy="13">Your Environment</tspan></text>

      <circle class="factor-dot" cx="168" cy="721" r="3"/>
      <text class="factor-label" x="175" y="725">Longevity</text>

      <circle class="factor-dot" cx="189" cy="633" r="3"/>
      <text class="factor-label" x="196" y="637">Sexual Health</text>

      <circle class="factor-dot" cx="244" cy="559" r="3"/>
      <text class="factor-label" x="254" y="563">Aesthetics –<tspan x="254" dy="13">Facial, Hair, Body</tspan></text>
    </g>
  </svg>
</main>
</body>
</html>
```